Postcard Design

business name: COZY NEST HELPERS. I am a mother of 2 well adjusted, successful teenage boys. I decided to start this company caring for kids who are home sick, unable to go to daycare or school, and when their parent cant stay home with them. I was also a career woman for many years, with no friends available or family nearby to help when i was in an emergency situation for childcare. I know how stressful it can be when a child gets sick suddenly and unexpectedly. I would like to help out those parents in need, that have pressing schedules and a sick child at home that they really want to take care of, but cant due to their work pressures and priorities. I want parents to know that their child is safe and I can help them when in need, at last minute. The design should show the child is safe and well cared for and the parent is at ease, able to accomplish their obligations. I have also founded a nonprofit environmental education program in which I teach children in youth summer camps. I have taught creativity arts combined with science curriculum in kindergarten to 8th grade non-formal teaching for the past 5 years. This is a small community, and many people know me. I will be handing out these postcards to local daycares and people I know.

Industry/Entity Type

Business

```html
<!DOCTYPE html>
<html lang="en">
<head>
<meta charset="utf-8">
<title>Cozy Nest Helpers – Postcard</title>
<link href="https://fonts.googleapis.com/css2?family=Oswald:wght@500;600&family=Roboto:ital,wght@1,400&family=Lato:wght@400;700&family=Archivo:wght@800&display=swap" rel="stylesheet">
<style>
  :root{
    --blue:#2b49a4;
    --blue-dark:#1f3586;
    --orange:#f7931e;
    --orange-light:#fdc23a;
    --yellow:#fde233;
    --pink:#e8358f;
    --green:#7cc242;
    --green-dark:#58a32c;
    --ink:#1e1e1e;
    --white:#ffffff;
    --page:#d9d9d9;
  }
  *{margin:0;padding:0;box-sizing:border-box}
  html,body{width:900px;height:1200px;overflow:hidden;background:var(--page)}
  .canvas{position:relative;width:900px;height:1200px}
  .card{position:absolute;left:98px;width:705px;height:545px;overflow:hidden;box-shadow:0 3px 8px rgba(0,0,0,.35)}
  .card svg.shapes{position:absolute;left:0;top:0}
  .card--front{top:38px;
    background:
      repeating-conic-gradient(from 0deg at 38% 62%, rgba(255,255,255,.09) 0 5deg, transparent 5deg 10deg),
      radial-gradient(circle at 38% 62%, var(--orange-light) 0, var(--orange) 60%);
  }
  .card--back{top:618px;background:var(--white)}
  .abs{position:absolute}

  .experience{left:24px;top:22px;color:var(--white)}
  .experience__years{font-family:"Archivo",sans-serif;font-weight:800;font-size:22px;color:var(--yellow);letter-spacing:.5px;line-height:26px}
  .experience__label{font-family:"Archivo",sans-serif;font-weight:800;font-size:16px;line-height:22px;letter-spacing:.2px}

  .headline{left:24px;top:130px;line-height:1}
  .headline__top{font-family:"Oswald",sans-serif;font-weight:600;font-size:54px;color:var(--ink);display:block;letter-spacing:.5px}
  .headline__bottom{font-family:"Roboto",sans-serif;font-style:italic;font-weight:400;font-size:52px;color:var(--white);display:block;margin-top:-2px;letter-spacing:1px}

  .front-copy{left:26px;top:255px;width:263px;font-family:"Lato",sans-serif;font-size:13.2px;line-height:16.7px;color:var(--ink);text-align:justify;hyphens:auto}

  .badge-text{left:496px;top:301px;width:108px;text-align:center;font-family:"Archivo",sans-serif;font-weight:800;font-size:19.5px;line-height:26.5px;color:var(--ink);white-space:nowrap}

  .footer{left:0;top:490px;width:705px;display:flex;align-items:center;color:var(--white);font-family:"Lato",sans-serif;font-weight:700;font-size:20px}
  .footer__name{margin-left:29px}
  .footer__phone{margin-left:24px;font-size:21px}
  .footer__web{margin-left:20px;display:flex;align-items:center;gap:7px;font-size:20.5px}

  .name-tab{left:0;top:165px;width:130px;height:26px;background:var(--green);border-radius:0 13px 13px 0;border:2px solid #b6e28e;border-left:0;font-family:"Lato",sans-serif;font-weight:700;font-size:14.5px;color:var(--ink);padding:3px 0 0 21px}
  .back-copy{left:22px;top:205px;width:292px;font-family:"Lato",sans-serif;font-size:14.4px;line-height:19px;color:var(--ink);text-align:justify}
  .cta{left:22px;top:370px}
  .cta__lead{font-family:"Oswald",sans-serif;font-weight:500;font-size:20px;color:var(--white);line-height:28px}
  .cta__alt{font-family:"Archivo",sans-serif;font-weight:800;font-size:18px;color:var(--ink);line-height:28px}
  .cta__call{display:flex;align-items:baseline;gap:10px;white-space:nowrap}
  .cta__call-label{font-family:"Oswald",sans-serif;font-weight:500;font-size:30px;letter-spacing:-.5px;color:var(--white)}
  .cta__phone{font-family:"Archivo",sans-serif;font-weight:800;font-size:17px;color:var(--ink)}
  .back-footer{left:22px;top:486px;color:var(--white);font-family:"Lato",sans-serif;font-size:15.5px;line-height:22px}
  .back-footer__web{display:flex;align-items:center;gap:7px}
  .stamp-box{left:602px;top:37px;width:63px;height:86px;border:1.5px solid #555}
</style>
</head>
<body>
<div class="canvas">

  <section class="card card--front">
    <svg class="shapes" width="705" height="545" viewBox="0 0 705 545">
      <defs>
        <linearGradient id="blueBand" x1="0" y1="0" x2="1" y2="0">
          <stop offset="0" stop-color="#2f4fae"/><stop offset="1" stop-color="#233f98"/>
        </linearGradient>
        <linearGradient id="photoTone" x1="0" y1="0" x2="1" y2="1">
          <stop offset="0" stop-color="#e9dcc8"/><stop offset=".55" stop-color="#d9bfa4"/><stop offset="1" stop-color="#f1ece4"/>
        </linearGradient>
        <radialGradient id="badgeGreen" cx=".45" cy=".4" r=".7">
          <stop offset="0" stop-color="#b4e05a"/><stop offset="1" stop-color="#6cb533"/>
        </radialGradient>
      </defs>
      <path d="M0 0 H300 C290 40 282 75 278 96 Q150 104 0 122 Z" fill="url(#blueBand)"/>
      <path d="M0 124 Q150 104 280 98" fill="none" stroke="var(--pink)" stroke-width="4"/>
      <path d="M0 131 Q150 111 282 105" fill="none" stroke="var(--green)" stroke-width="4"/>
      <ellipse cx="512" cy="118" rx="234" ry="222" fill="none" stroke="var(--green)" stroke-width="10"/>
      <ellipse cx="512" cy="118" rx="224" ry="212" fill="none" stroke="var(--yellow)" stroke-width="4"/>
      <ellipse cx="512" cy="118" rx="219" ry="207" fill="none" stroke="var(--pink)" stroke-width="5"/>
      <ellipse cx="512" cy="118" rx="214" ry="202" fill="url(#photoTone)" role="img" aria-label="Photo: a caregiver gently checking a sick child's temperature as the child rests in bed"/>
      <path d="M0 466 Q350 402 705 474" fill="none" stroke="var(--pink)" stroke-width="4"/>
      <path d="M0 474 Q350 410 705 482" fill="none" stroke="var(--green)" stroke-width="4"/>
      <path d="M0 481 Q350 417 705 489 V545 H0 Z" fill="url(#blueBand)"/>
      <g class="badge" fill="url(#badgeGreen)" stroke="#ffffff" stroke-width="3">
        <circle cx="550" cy="354" r="72"/>
      </g>
      <g fill="#7fc43a">
        <circle cx="550" cy="354" r="64"/>
        <circle cx="614" cy="354" r="12"/><circle cx="609" cy="378" r="12"/><circle cx="595" cy="399" r="12"/>
        <circle cx="574" cy="413" r="12"/><circle cx="550" cy="418" r="12"/><circle cx="526" cy="413" r="12"/>
        <circle cx="505" cy="399" r="12"/><circle cx="491" cy="378" r="12"/><circle cx="486" cy="354" r="12"/>
        <circle cx="491" cy="330" r="12"/><circle cx="505" cy="309" r="12"/><circle cx="526" cy="295" r="12"/>
        <circle cx="550" cy="290" r="12"/><circle cx="574" cy="295" r="12"/><circle cx="595" cy="309" r="12"/>
        <circle cx="609" cy="330" r="12"/>
      </g>
      <circle cx="545" cy="345" r="50" fill="#a6d84e" opacity=".6"/>
    </svg>

    <div class="abs experience">
      <div class="experience__years">OVER 14 YEARS</div>
      <div class="experience__label">CHILD CARE EXPERIENCE</div>
    </div>

    <h1 class="abs headline">
      <span class="headline__top">COZY NEST</span>
      <span class="headline__bottom">HELPERS</span>
    </h1>

    <p class="abs front-copy">Most parents have experienced a time when they have needed trustworthy, last minute care for a sick child who cannot attend school or daycare. Some parents may have a designated caretaker become ill or have schedule conflicts. During this critical time when your child is recuperating, or you need last minute childcare, parents can trust Mara Lindqvist who is experienced in providing compassionate care.</p>

    <p class="abs badge-text">But you<br>must go<br>to work<br>today</p>

    <div class="abs footer">
      <span class="footer__name">Mara Lindqvist</span>
      <span class="footer__phone">(206) 555-0147</span>
      <span class="footer__web">
        <svg width="11" height="11" viewBox="0 0 12 12"><circle cx="6" cy="6" r="5.5" fill="#f2b233"/><path d="M0.5 6H11.5M6 .5V11.5M2 3H10M2 9H10" stroke="#8a5a00" stroke-width=".8" fill="none"/></svg>
        www.nestsitters.net/p/mara/cc
      </span>
    </div>
  </section>

  <section class="card card--back">
    <svg class="shapes" width="705" height="545" viewBox="0 0 705 545">
      <defs>
        <radialGradient id="backOrange" cx=".35" cy=".45" r=".8">
          <stop offset="0" stop-color="var(--orange-light)"/><stop offset="1" stop-color="var(--orange)"/>
        </radialGradient>
      </defs>
      <path d="M244 0 C338 70 388 190 380 300 C372 366 355 420 338 472" fill="none" stroke="var(--green)" stroke-width="10"/>
      <path d="M233 0 C327 70 377 190 369 300 C361 366 344 420 327 472" fill="none" stroke="var(--blue)" stroke-width="6"/>
      <path d="M0 0 H226 C320 70 370 190 362 300 C354 366 337 420 320 472 H0 Z" fill="url(#backOrange)"/>
      <rect x="0" y="472" width="334" height="73" fill="var(--blue)"/>
      <circle cx="86" cy="88" r="63" fill="var(--white)"/>
      <circle cx="86" cy="88" r="60" fill="none" stroke="var(--blue)" stroke-width="4"/>
      <circle cx="86" cy="88" r="56" fill="#cfc6c0" role="img" aria-label="Portrait photo of the caregiver"/>
    </svg>

    <div class="abs name-tab">Mara Lindqvist</div>

    <p class="abs back-copy">I am a 10-year resident, Cedar Harbor Island mom, who would like to help parents in need. As an Island parent, I have been there, and know how logistics and illness can cause stressful situations. You can count on me when your child gets sick and you need a backup. I can also work as a fill-in when your nanny is sick.</p>

    <div class="abs cta">
      <div class="cta__lead">For your last minute request</div>
      <div class="cta__alt">Or advanced scheduling</div>
      <div class="cta__call"><span class="cta__call-label">Call Mara at</span><span class="cta__phone">(206) 555-0147</span></div>
    </div>

    <div class="abs back-footer">
      <div>Mara Lindqvist</div>
      <div class="back-footer__web">
        <svg width="10" height="10" viewBox="0 0 12 12"><circle cx="6" cy="6" r="5.5" fill="#f2b233"/><path d="M0.5 6H11.5M6 .5V11.5M2 3H10M2 9H10" stroke="#8a5a00" stroke-width=".8" fill="none"/></svg>
        www.nestsitters.net/p/mara/cc
      </div>
    </div>

    <div class="abs stamp-box"></div>
  </section>

</div>
</body>
</html>
```